Takeout menu

I need a takeout menu for Casa Lumo in Westerly RI. It needs just the location, phone number, items and descriptions from my square site- no pricing listed. No hours listed as I am seasonal and they change during the year. Must say "please inform us of any food allergies prior to ordering" somewhere on it, per order of health dept. I will most likely be printing in b/w.

```html
<!DOCTYPE html>
<html lang="en">
<head>
<meta charset="utf-8">
<title>Casa Lumo Takeout Menu</title>
<link href="https://fonts.googleapis.com/css2?family=Alfa+Slab+One&family=Archivo+Black&family=Montserrat:wght@400;500;700&display=swap" rel="stylesheet">
<style>
:root{
  --red:#e3001b;
  --ink:#1f2a36;
  --paper:#ffffff;
  --backdrop:#a0a0a0;
  --slice:#f0a800;
  --slice-deep:#e06a10;
  --sketch:#fdeef0;
}
*{margin:0;padding:0;box-sizing:border-box}
html,body{width:839px;height:1200px;overflow:hidden;background:var(--backdrop)}
.menu{position:absolute;left:111px;top:72px;width:616px;height:1056px;background:var(--paper);overflow:hidden;font-family:"Montserrat",sans-serif;color:var(--ink)}
.abs{position:absolute}
.header{left:0;top:0;width:616px;height:212px}
.art-slice{left:6px;top:37px;width:227px;height:152px;border-radius:6px 60px 6px 6px;background:linear-gradient(135deg,var(--slice),var(--slice-deep))}
.art-sketch{left:0;top:0;width:160px;height:80px;background:rgba(255,255,255,.18);border-radius:0 0 60px 0}
.art-lettering{left:241px;top:82px;width:337px;height:66px;background:rgba(255,255,255,.9);border-radius:30px}
.art-burst{left:330px;top:8px;width:110px;height:60px;background:radial-gradient(ellipse at 50% 100%,rgba(255,255,255,.35),rgba(255,255,255,0) 70%)}
.tagline{left:391px;top:62px;font-weight:700;font-size:21px;color:var(--paper);white-space:nowrap}
.menu-word{left:240px;top:150px;width:340px;display:flex;align-items:center;gap:12px}
.menu-word span{font-family:"Archivo Black",sans-serif;font-size:32px;letter-spacing:14px;color:var(--paper);line-height:1}
.menu-word i{flex:1;height:2px;background:var(--paper)}
.section-head{border-top:2px solid var(--ink);border-bottom:2px solid var(--ink);display:flex;align-items:center;justify-content:center;gap:8px}
.section-title{font-family:"Alfa Slab One",serif;color:var(--red);font-size:17px;letter-spacing:1.2px;line-height:1;white-space:nowrap}
.section-note{font-size:4.6px;color:var(--red);line-height:1.3}
.item h3{font-family:"Archivo Black",sans-serif;font-size:10.5px;letter-spacing:.3px;line-height:1;text-transform:uppercase;font-weight:400;white-space:nowrap}
.item p{font-size:6.5px;line-height:8.8px;margin-top:5px;font-weight:500;letter-spacing:-.15px}
.rule-dash-v{border-left:1px dashed var(--ink)}
.rule-dash-h{border-top:1px dashed var(--ink)}
.order-title{left:45px;top:899px;font-family:"Archivo Black",sans-serif;font-size:22px;color:var(--red);letter-spacing:.5px;line-height:1.2}
.phone{left:45px;top:926px;display:flex;align-items:center;gap:14px}
.phone span{font-family:"Archivo Black",sans-serif;font-size:38px;color:var(--ink);letter-spacing:-.5px;line-height:1}
.address{left:47px;top:972px;display:flex;align-items:center;gap:12px}
.address span{font-family:"Archivo Black",sans-serif;font-size:13px;color:var(--ink);letter-spacing:.3px;white-space:nowrap}
.art-outline-slice{left:514px;top:814px;width:108px;height:196px;background:linear-gradient(160deg,var(--sketch),#fbe3e6);border-radius:40px 0 0 60px}
.art-leaf{left:20px;top:877px;width:12px;height:16px;background:#8cb544;border-radius:50% 50% 40% 60%}
.footer-band{left:0;top:1014px;width:616px;height:42px;background:var(--ink);display:flex;align-items:center;justify-content:center}
.footer-band p{color:var(--paper);font-size:12px;font-weight:500}
</style>
</head>
<body>
<main class="menu">
  <svg class="abs header" viewBox="0 0 616 212" aria-hidden="true">
    <path d="M0 0H616V200L600 196 585 203 560 195 540 202 515 196 490 204 460 195 430 203 400 196 370 204 340 197 310 205 280 196 250 203 220 196 190 204 160 196 130 202 100 195 70 203 40 196 15 201 0 197Z" fill="var(--red)"/>
  </svg>
  <div class="abs art-sketch" role="img" aria-label="White line sketch of a pizza slice"></div>
  <div class="abs art-slice" role="img" aria-label="Illustrated pepperoni pizza slice flying with cheese drips"></div>
  <div class="abs art-burst" role="img" aria-label="Sunburst lines"></div>
  <div class="abs art-lettering" role="img" aria-label="Hand-lettered word Takeout"></div>
  <div class="abs tagline">Locally owned</div>
  <div class="abs menu-word"><i></i><span>MENU</span><i></i></div>

  <div class="abs section-head" style="left:45px;top:226px;width:335px;height:30px">
    <span class="section-title">RED PIZZAS</span><span class="section-note">all pizzas are 14"</span>
  </div>
  <div class="abs item" style="left:45px;top:271px;width:170px"><h3>Mozzarella</h3><p>crushed tomato sauce, shredded whole milk mozzarella, grated parmesan and pecorino cheeses, garlic infused extra virgin olive oil</p></div>
  <div class="abs item" style="left:45px;top:334px;width:170px"><h3>The Vinci</h3><p>shredded whole milk mozzarella, fresh mozzarella, fresh basil, sauce on top, grated parmesan and pecorino, garlic oil. This is similar to a NY-style margherita pizza</p></div>
  <div class="abs item" style="left:45px;top:406px;width:170px"><h3>Toscano</h3><p>Bar-style (flat and crispy) pizza with whole-milk mozzarella, pecorino, parmesan, crushed tomato sauce on top, garlic-infused extra virgin oil, and seasoned with oregano and crushed red chili flakes.</p></div>
  <div class="abs item" style="left:45px;top:476px;width:170px"><h3>Meatball Combo</h3><p>mozzarella pie base, slices of house-made meatballs, roasted peppers, and sautéed onions</p></div>
  <div class="abs item" style="left:45px;top:526px;width:170px"><h3>West Coast Combo</h3><p>Mozzarella pie with sliced local sausage, roasted mushrooms, and black olives</p></div>
  <div class="abs item" style="left:45px;top:580px;width:170px"><h3>Pepperoni Supreme</h3><p>mozzarella pie base with roasted mushrooms, and vinegar peppers</p></div>
  <div class="abs item" style="left:45px;top:634px;width:170px"><h3>Gar-Leek</h3><p>mozzarella pie base, garlic confit, buttery leeks</p></div>

  <div class="abs item" style="left:228px;top:271px;width:152px"><h3>Pepperoni</h3><p>mozzarella pie base, pepperoni cups</p></div>
  <div class="abs item" style="left:228px;top:317px;width:152px"><h3>Margherita</h3><p>crushed tomato sauce, fresh mozzarella, fresh basil, parmesan, pecorino, garlic oil</p></div>
  <div class="abs item" style="left:228px;top:370px;width:152px"><h3>Sausage Combo</h3><p>mozzarella pie base, cup &amp; char sausage, roasted peppers, sautèed onions</p></div>
  <div class="abs item" style="left:228px;top:423px;width:152px"><h3>Soupy Combo</h3><p>mozzarella pie base, local soppressata, roasted peppers, sautèed onions</p></div>
  <div class="abs item" style="left:228px;top:475px;width:152px"><h3>El Jefe</h3><p>Mozzarella pizza with cup and char sausage, roasted onions, and banana peppers</p></div>
  <div class="abs item" style="left:228px;top:527px;width:140px"><h3>Hawaiian</h3><p>pepperoni pie base, roasted green hatch chiles (medium spice level), fresh cut pineapple</p></div>
  <div class="abs item" style="left:228px;top:587px;width:140px"><h3>Towner</h3><p>Start with a Toscano pie, then add roasted tomatoes, buttery leeks, and house-made meatball</p></div>

  <div class="abs rule-dash-v" style="left:392px;top:226px;height:440px"></div>

  <div class="abs section-head" style="left:408px;top:226px;width:158px;height:30px">
    <span class="section-title">WHITE PIZZAS</span>
  </div>
  <div class="abs item" style="left:408px;top:271px;width:164px"><h3>White</h3><p>shredded mozzarella, fresh mozzarella, pecorino, parmesan, ricotta, fresh basil, garlic oil (no sauce)</p></div>
  <div class="abs item" style="left:408px;top:320px;width:150px"><h3>Spinach B.L.T.</h3><p>spinach pie base, buttery leeks, bacon, roasted tomato</p></div>
  <div class="abs item" style="left:408px;top:367px;width:158px"><h3>Potato Pie</h3><p>sliced russets, buttery leeks, fresh mozzarella, medium cheddar, bacon, parmesan, pecorino, garlic oil (no sauce)</p></div>
  <div class="abs item" style="left:408px;top:426px;width:166px"><h3>Apple Pie</h3><p>medium cheddar, parmesan, pecorino, tart apples, bacon, fresh mozzarella, sautèed onions, garlic oil, and comes with a side of hot honey to drizzle</p></div>
  <div class="abs item" style="left:408px;top:487px;width:162px"><h3>Spinach</h3><p>white pie base, baby spinach, garlic confit</p></div>
  <div class="abs item" style="left:408px;top:533px;width:158px"><h3>Veggie</h3><p>white pie base with fresh spinach, roasted mushrooms, roasted peppers, sautèed onions, roasted tomatoes</p></div>
  <div class="abs item" style="left:408px;top:592px;width:162px"><h3>Chicken Bacon Ranch</h3><p>shredded mozzarella, cheddar, roasted chicken, bacon, leeks, roasted tomatoes, ranch drizzle</p></div>

  <div class="abs rule-dash-h" style="left:45px;top:666px;width:528px"></div>
  <div class="abs rule-dash-v" style="left:392px;top:676px;height:320px"></div>

  <div class="abs section-head" style="left:45px;top:683px;width:335px;height:29px">
    <span class="section-title">CUSTOM PIZZA</span><span class="section-note" style="width:125px">Start with either our red or white pie and add what you'd like! Build your own whole pie or half/half!</span>
  </div>
  <div class="abs item" style="left:45px;top:731px;width:160px"><h3>BYOP Mozzarella</h3><p>starts with crushed tomato sauce, shredded mozzarella, parmesan, pecorino, garlic oil</p></div>
  <div class="abs item" style="left:228px;top:731px;width:140px"><h3>BYOP White</h3><p>starts with shredded mozzarella, fresh mozzarella, pecorino, parmesan, ricotta, fresh basil, garlic oil (no sauce)</p></div>

  <div class="abs section-head" style="left:45px;top:786px;width:335px;height:29px">
    <span class="section-title">GREENS</span>
  </div>
  <div class="abs item" style="left:45px;top:830px;width:160px"><h3>Caesar Salad</h3><p>With house-made sourdough croutons, shaved parmesan, lemon wedge, and 2 house-made Caesar dressings</p></div>
  <div class="abs item" style="left:228px;top:830px;width:150px"><h3>Chop Salad</h3><p>Mixed greens, diced chicken, bacon, gorgonzola, ditalini pasta, red onion, roasted tomatoes, with 2 sides of house-made balsamic vinaigrette</p></div>

  <div class="abs rule-dash-h" style="left:45px;top:884px;width:341px"></div>
  <div class="abs art-leaf" role="img" aria-label="Basil leaf"></div>

  <div class="abs order-title">ORDER ONLINE</div>
  <div class="abs phone">
    <svg width="30" height="30" viewBox="0 0 24 24" aria-hidden="true"><path fill="var(--red)" d="M6.6 2.2 9.4 5.8c.5.6.4 1.5-.1 2L7.6 9.4c1.2 2.8 3.4 5 6.2 6.3l1.6-1.6c.6-.6 1.4-.6 2-.1l3.6 2.8c.7.5.8 1.5.2 2.1l-2 2.1c-.8.8-2 1.1-3.1.7C9.7 19.6 4.5 14.4 2.4 8.1c-.4-1.1-.1-2.3.7-3.1l2-2c.5-.5 1.2-.5 1.5-.8z"/></svg>
    <span>401.555.0148</span>
  </div>
  <div class="abs address">
    <svg width="14" height="19" viewBox="0 0 14 19" aria-hidden="true"><path fill="var(--red)" d="M7 0C3.1 0 0 3.1 0 7c0 5 7 12 7 12s7-7 7-12c0-3.9-3.1-7-7-7zm0 10a3 3 0 1 1 0-6 3 3 0 0 1 0 6z"/></svg>
    <span>12 HARBOR LANE PORT AVERY, RI 02999</span>
  </div>

  <div class="abs art-outline-slice" role="img" aria-label="Red line drawing of a pizza slice"></div>
  <div class="abs section-head" style="left:408px;top:683px;width:158px;height:29px">
    <span class="section-title">SIDES</span>
  </div>
  <div class="abs item" style="left:408px;top:731px;width:160px"><h3>Fries</h3><p style="margin-top:3px">house-cut!</p></div>
  <div class="abs item" style="left:408px;top:767px;width:166px"><h3>Garlic Focaccia Bread</h3><p>A lightly stretched dough, shredded whole milk mozzarella, pecorino and parmesan cheeses, and lots of garlic infused extra virgin olive oil. comes with a side of house-made marinara</p></div>
  <div class="abs item" style="left:408px;top:836px;width:100px"><h3>Fruit Sodas</h3><p>Choose a flavor</p></div>
  <div class="abs item" style="left:408px;top:878px;width:104px"><h3>Wings</h3><p>6 crispy wingdings tossed in your choice of sauce, or plain</p></div>
  <div class="abs item" style="left:408px;top:929px;width:130px"><h3>Chicken Nuggets</h3><p>For the kids! 10 piece</p></div>
  <div class="abs item" style="left:408px;top:970px;width:100px"><h3>Soda</h3><p>12oz can. Choose a flavor</p></div>

  <svg class="abs" style="left:0;top:1000px" width="616" height="16" viewBox="0 0 616 16" aria-hidden="true">
    <path d="M0 16V8L20 4 45 9 70 3 100 10 130 5 160 11 190 4 220 10 250 5 280 11 310 4 340 10 370 3 400 9 430 5 460 11 490 4 520 9 550 3 580 10 616 6V16Z" fill="var(--ink)"/>
  </svg>
  <div class="abs footer-band"><p>Please note: please inform us of any food allergies prior to ordering</p></div>
</main>
</body>
</html>
```